Korvanta Business Card

Looking for business card ideas. Company name is Korvanta. Have a few basic ideas on attachment. Please submit anything with the logo and general information from attachment.

Industry/Entity Type

Business

```html
<!DOCTYPE html>
<html lang="en">
<head>
<meta charset="utf-8">
<title>Korvanta Business Card</title>
<link rel="stylesheet" href="https://fonts.googleapis.com/css2?family=Source+Sans+3:wght@400;600&display=swap">
<style>
  :root {
    --paper: #ffffff;
    --ink: #1e1e1e;
    --brand-red: #e8141b;
    --rule-red: #e3161c;
    --font-main: "Source Sans 3", Arial, sans-serif;
  }
  * { margin: 0; padding: 0; box-sizing: border-box; }
  html, body {
    width: 1200px;
    height: 686px;
    overflow: hidden;
    background: var(--paper);
  }
  .card {
    position: relative;
    width: 1200px;
    height: 686px;
    background: var(--paper);
    font-family: var(--font-main);
    color: var(--ink);
  }
  .brand-name {
    position: absolute;
    left: 64px;
    top: 62px;
    font-size: 136px;
    font-weight: 600;
    color: var(--brand-red);
    letter-spacing: 4px;
    line-height: 1;
  }
  .tagline-block {
    position: absolute;
    right: 78px;
    top: 290px;
    text-align: right;
    font-size: 27px;
    line-height: 38px;
  }
  .divider {
    position: absolute;
    left: 80px;
    top: 390px;
    width: 1064px;
    height: 16px;
  }
  .contact {
    position: absolute;
    top: 474px;
    font-size: 30px;
    line-height: 45px;
  }
  .contact-left { left: 84px; }
  .contact-right { right: 78px; text-align: right; }
  .phone-label { display: inline-block; margin-left: 18px; }
</style>
</head>
<body>
  <div class="card">
    <div class="brand-name">Korvanta</div>

    <div class="tagline-block">
      <p class="tagline">Taking Churches to the NEXT Level</p>
      <p class="person">Dale Hovins, Dir.</p>
    </div>

    <svg class="divider" viewBox="0 0 1064 16" preserveAspectRatio="none" aria-hidden="true">
      <defs>
        <linearGradient id="rule-fade" x1="0" x2="1" y1="0" y2="0">
          <stop offset="0" stop-color="#e3161c" stop-opacity="0.2"/>
          <stop offset="0.08" stop-color="#e3161c" stop-opacity="1"/>
          <stop offset="0.92" stop-color="#e3161c" stop-opacity="1"/>
          <stop offset="1" stop-color="#e3161c" stop-opacity="0.2"/>
        </linearGradient>
      </defs>
      <path d="M0 8 Q532 2 1064 8 Q532 12 0 8 Z" fill="url(#rule-fade)"/>
    </svg>

    <div class="contact contact-left">
      <p>(555) 210-4830<span class="phone-label">Office</span></p>
      <p>(555) 374-9162<span class="phone-label">Cell</span></p>
      <p>dhovins@korvanta.org</p>
    </div>

    <div class="contact contact-right">
      <p>2480 N. Alder Ave.</p>
      <p>Marlow, TX 79000</p>
      <p>www.korvanta.org</p>
    </div>
  </div>
</body>
</html>
```